K&T Fire Safety Equipment Inc. needs an updated/new website design

I would like the customer to be able to see who we are, where are are, what we do and areas we cover on the first page. I would like something modern but professional. The other fire safety companies out there have very boring & unappealing websites. I want mine seem like we've got it together and to be above average in comparison. I would like the colors to go with our logo and would like to incorporate somewhere that we have been in business for over 30 years, we are family owned and operated and that we provide service to all of central Florida from Tampa to Titusville and all of Brevard county (we can take out the" all of Brevard county" but keep the " All of Central Florida from Tampa to Titusville" and just add all counties we service to the very bottom too). We are a residential and commercial fire safety equipment company. We do sales, service and installation for fire extinguishers, emergency/exit lighting, kitchen fire suppression systems, fire alarms & fire extinguisher cabinets.I have also attached some pictures that you can use to incorporate any way you would like. Here's our current website (awful I know) to get information from if needed. kandtfiresafety.example

Target Market(s)

Restaurants, hotels, vacation rental properties & small businesses. Every business is required to have a fire extinguisher and exit lighting.

Industry/Entity Type

Fire Safety

Number of Pages Required

1 page

Font styles to use
Other font styles liked:
• I'm open to your suggestions

Colors

Designer to choose colors to be used in the design.

Requirements
Must have
• I would like the customer to be able to see who we are, where are are, what we do and areas we cover on the first page. I would like the colors to go with our logo and would like to incorporate somewhere that we have been in business for over 30 years, we are family owned and operated and that we provide service to all of central Florida from Tampa to Titusville and all of Brevard county (we can take out the" all of Brevard county" but keep the " All of Central Florida from Tampa to Titusville" and just add all counties we service to the very bottom too)
Nice to have
• Modern with high quality pictures
• I love the raised logo that I added in the attachments. If you could make the logo look like that in incorporate it as one of the first things you see that would be awesome!
• I would eventually like to have a portfolio of work completed on an additional page.
Should not have
• boring outdated look

```html
<!DOCTYPE html>
<html lang="en">
<head>
<meta charset="utf-8">
<title>K&amp;T Fire Safety Equipment Inc.</title>
<link rel="stylesheet" href="https://fonts.googleapis.com/css2?family=Poppins:wght@400;500;600&family=Roboto+Condensed:wght@300;400;700&display=swap">
<style>
:root{
  --orange:#ee5a0c;
  --ink:#1b1b1b;
  --dark:#141414;
  --darker:#0d0d0d;
  --grey:#3a3a3a;
  --text:#4a4a4a;
  --line:#dcdcdc;
  --white:#ffffff;
}
*{box-sizing:border-box;margin:0;padding:0}
html,body{width:1200px;height:2857px;overflow:hidden}
body{position:relative;background:var(--white);font-family:"Poppins",sans-serif;color:var(--text)}
.abs{position:absolute}
.topbar{left:0;top:0;width:1200px;height:36px;background:var(--ink);color:#ddd;font-size:12px}
.topbar .item{position:absolute;top:10px;display:flex;align-items:center;gap:10px;white-space:nowrap;line-height:16px}
.topbar .dot{width:16px;height:16px;border-radius:50%;background:var(--orange);display:inline-block;flex:none}
.topbar .socials{position:absolute;right:54px;top:10px;display:flex;gap:18px}
.header{left:0;top:36px;width:1200px;height:82px;background:var(--white)}
.brand{position:absolute;left:86px;top:22px;display:flex;align-items:center;gap:12px}
.brand .mark{width:36px;height:36px;background:var(--orange)}
.brand .name{font-family:"Roboto Condensed",sans-serif;font-weight:700;font-size:22px;color:var(--ink);text-transform:uppercase;letter-spacing:.5px}
.dial{position:absolute;left:741px;top:23px;height:36px;display:flex;font-size:14px}
.dial .label{background:var(--orange);color:var(--white);width:128px;display:flex;align-items:center;justify-content:center}
.dial .nums{background:var(--grey);color:var(--white);width:245px;display:flex;align-items:center;justify-content:center}
.nav{left:0;top:118px;width:1200px;height:44px;border-top:1px solid #e6e6e6;background:var(--white)}
.nav ul{list-style:none;position:absolute;left:234px;top:0;display:flex;height:44px;align-items:center;font-family:"Roboto Condensed",sans-serif;font-size:15px;color:var(--ink)}
.nav li{position:relative;text-align:center}
.nav li.active{background:var(--orange);color:var(--white);height:44px;line-height:44px;width:122px}
.nav li.sep::before{content:"|";position:absolute;left:-8px;color:#999}
.hero{left:0;top:162px;width:1200px;height:644px;background:linear-gradient(180deg,#1d2a5a 0%,#4a4d7a 35%,#6c5a7c 52%,#2a2a3a 60%,#3c3540 75%,#24232e 100%)}
.hero-panel{left:571px;top:330px;width:543px;height:318px;background:rgba(40,40,48,.55);text-align:right;padding:50px 42px 0 0;color:var(--white);font-family:"Roboto Condensed",sans-serif;text-transform:uppercase}
.hero-panel .l1{font-weight:300;font-size:52px;line-height:60px}
.hero-panel .l2{font-weight:400;font-size:66px;line-height:78px}
.hero-panel .l3{font-size:66px;line-height:78px}
.hero-panel .l3 span{font-weight:300;font-size:48px}
.intro{left:132px;top:884px;width:936px;text-align:center;font-size:16px;line-height:39px;color:var(--text)}
.corner{background:var(--orange)}
.btn{display:flex;align-items:center;justify-content:center;background:var(--orange);color:var(--white);font-family:"Roboto Condensed",sans-serif}
.services{left:86px;top:1250px;width:1028px;height:335px;background:radial-gradient(ellipse at 50% 40%,#2a1a14 0%,#111 60%,#0a0a0a 100%)}
.svc{position:absolute;top:0;width:343px;height:335px;text-align:center;color:var(--white)}
.svc .icon{width:116px;height:116px;border-radius:50%;background:var(--orange);margin:46px auto 0;display:flex;align-items:center;justify-content:center}
.svc h3{font-family:"Roboto Condensed",sans-serif;font-weight:400;font-size:28px;margin-top:30px}
.svc .more{width:120px;height:42px;border:1px solid #bbb;margin:24px auto 0;font-size:13px;line-height:40px}
.svc-div{top:56px;width:1px;height:230px;background:#333}
.arrow{width:46px;height:46px}
.gallery-title{left:0;top:1620px;width:1200px;text-align:center;font-family:"Roboto Condensed",sans-serif;font-weight:400;font-size:52px;line-height:64px;color:var(--ink)}
.rule{top:1657px;height:1px;background:#cfcfcf}
.photo{position:absolute}
.quote{left:86px;top:2315px;width:1028px;height:125px;background:var(--orange);color:var(--white)}
.avatar{left:121px;top:2287px;width:138px;height:138px;border-radius:50%;border:5px solid var(--white);background:linear-gradient(160deg,#e9c99a,#c78f6a)}
.quote p{position:absolute;left:212px;top:34px;font-size:15px;line-height:24px;white-space:nowrap}
.quote small{position:absolute;left:212px;top:74px;font-size:12px;line-height:16px;letter-spacing:.5px;opacity:.85;white-space:nowrap}
.footer{left:0;top:2446px;width:1200px;height:351px;background:var(--dark);color:#ddd}
.footer h4{position:absolute;top:83px;font-size:13px;font-weight:400;color:var(--white);letter-spacing:.3px}
.footer h4::after{content:"";position:absolute;left:0;top:26px;width:52px;height:2px;background:var(--orange)}
.contact-row{position:absolute;left:86px;display:flex;gap:22px;align-items:flex-start;font-size:12px;line-height:17px}
.contact-row .ic{width:30px;height:30px;border-radius:50%;border:1px solid #666;display:flex;align-items:center;justify-content:center;flex:none}
.post{position:absolute;left:425px;width:220px;font-size:11.5px;line-height:17px}
.post .date{color:#bbb;font-size:11px;margin-bottom:10px}
.links{left:741px;top:2571px;list-style:none;font-size:12.5px;line-height:30px;color:var(--white)}
.vdiv{top:2560px;width:1px;height:200px;background:#2c2c2c}
.news-input{left:928px;top:2576px;width:140px;height:26px;border:1px solid #777;font-size:10px;color:#aaa;padding:6px 14px}
.news-go{left:1074px;top:2576px;width:36px;height:26px;font-size:11px}
.soc{top:2640px;width:24px;height:24px;border-radius:50%;background:var(--white)}
.copy{left:0;top:2797px;width:1200px;height:60px;background:var(--darker);border-top:1px solid #2a2a2a;text-align:center;line-height:60px;font-size:12px;color:#aaa}
</style>
</head>
<body>

<div class="abs topbar">
  <div class="item" style="left:86px"><span class="dot"></span>info@kandtfiresafety.example</div>
  <div class="item" style="left:318px"><span class="dot"></span>1-407-555-0142</div>
  <div class="socials"><span class="dot"></span><span class="dot"></span><span class="dot"></span><span class="dot"></span><span class="dot"></span></div>
</div>

<header class="abs header">
  <div class="brand"><span class="mark"></span><span class="name">K&amp;T Fire Safety Equipment Inc.</span></div>
  <div class="dial"><div class="label">Emergency Dial</div><div class="nums">1-407-555-0187 / 1-407-555-0163</div></div>
</header>

<nav class="abs nav">
  <ul>
    <li class="active">HOME</li>
    <li style="width:150px">SERVICES</li>
    <li class="sep" style="width:180px">TESTIMONIALS</li>
    <li class="sep" style="width:110px">JOBS</li>
    <li class="sep" style="width:150px">CONTACT US</li>
  </ul>
</nav>

<section class="abs hero" role="img" aria-label="Night city skyline reflected on the water"></section>
<div class="abs hero-panel">
  <div class="l1">Dedicated to</div>
  <div class="l2">Protecting Life</div>
  <div class="l3"><span>and</span> Property</div>
</div>

<div class="abs corner" style="left:106px;top:867px;width:76px;height:4px"></div>
<div class="abs corner" style="left:104px;top:867px;width:4px;height:80px;background:var(--ink)"></div>
<p class="abs intro">We have been providing fire protection to Central Florida for over 30 years! &nbsp;K &amp; T Fire Safety is family owned and operated. We provide quality service, professional fire protection and life safety to meet the needs of our community. We provide residential and commercial fire protection to all of Brevard County and Central Florida from Tampa to Titusville. &nbsp;Our staff is exceptionally knowledgeable in fire safety and protection. Please feel free to contact us with any questions or concerns.</p>
<div class="abs" style="left:1088px;top:995px;width:4px;height:80px;background:var(--ink)"></div>
<div class="abs corner" style="left:1012px;top:1072px;width:80px;height:4px"></div>
<div class="abs btn" style="left:516px;top:1122px;width:172px;height:55px;font-size:21px">Learn More</div>

<svg class="abs arrow" style="left:16px;top:1385px" viewBox="0 0 46 46"><circle cx="23" cy="23" r="21" fill="none" stroke="#bbb" stroke-width="2"/><path d="M32 23H14M21 15l-8 8 8 8" fill="none" stroke="#bbb" stroke-width="2"/></svg>
<svg class="abs arrow" style="left:1132px;top:1385px" viewBox="0 0 46 46"><circle cx="23" cy="23" r="21" fill="none" stroke="#bbb" stroke-width="2"/><path d="M14 23h18M25 15l8 8-8 8" fill="none" stroke="#bbb" stroke-width="2"/></svg>

<section class="abs services">
  <div class="svc" style="left:0">
    <div class="icon"><svg width="50" height="50" viewBox="0 0 50 50" fill="#fff"><path d="M15 34a10 10 0 0 1 20 0z"/><rect x="10" y="35" width="30" height="5"/><rect x="24" y="8" width="2" height="8"/><path d="M10 14l5 5-1.4 1.4-5-5zM40 14l-5 5 1.4 1.4 5-5z"/><rect x="3" y="26" width="7" height="2"/><rect x="40" y="26" width="7" height="2"/></svg></div>
    <h3>Emergency Lighting</h3>
    <div class="more">Learn More</div>
  </div>
  <div class="abs svc-div" style="left:336px"></div>
  <div class="svc" style="left:343px">
    <div class="icon"><svg width="50" height="50" viewBox="0 0 50 50" fill="none" stroke="#fff" stroke-width="3"><path d="M10 10l10 10M40 10L30 20M10 40l10-10M40 40L30 30"/><path d="M20 13v7h-7M30 13v7h7M20 37v-7h-7M30 37v-7h7"/></svg></div>
    <h3>Emergency Signage</h3>
    <div class="more">Learn More</div>
  </div>
  <div class="abs svc-div" style="left:684px"></div>
  <div class="svc" style="left:685px">
    <div class="icon"><svg width="50" height="50" viewBox="0 0 50 50" fill="none" stroke="#fff" stroke-width="2.5"><rect x="19" y="16" width="13" height="28" rx="3"/><path d="M22 16v-5h7v5M29 11h8l3 4M22 11l-6 4v6"/></svg></div>
    <h3>Extinguisher Signage</h3>
    <div class="more">Learn More</div>
  </div>
</section>

<div class="abs rule" style="left:92px;width:396px"></div>
<h2 class="abs gallery-title">Gallery</h2>
<div class="abs rule" style="left:718px;width:396px"></div>

<div class="photo" role="img" aria-label="Firefighter in turnout gear carrying a red hose" style="left:86px;top:1724px;width:325px;height:488px;background:linear-gradient(160deg,#2c3344,#b23a2a 55%,#c9c24a)"></div>
<div class="photo" role="img" aria-label="Technician servicing a fire alarm control panel" style="left:436px;top:1724px;width:326px;height:232px;background:linear-gradient(135deg,#8a6a4a,#2a3140 55%,#c8c8c8)"></div>
<div class="photo" role="img" aria-label="Kitchen fire suppression nozzles above a cooking line" style="left:787px;top:1724px;width:325px;height:232px;background:linear-gradient(135deg,#7a7a7a,#c9c9c9 40%,#b8473a 75%,#6a6a6a)"></div>
<div class="photo" role="img" aria-label="Hand holding the hose of a red fire extinguisher" style="left:436px;top:1981px;width:676px;height:231px;background:linear-gradient(90deg,#3a6fa8,#dca98a 35%,#e8d8d0 60%,#c62b2b)"></div>

<section class="abs quote">
  <p>Lorem Ipsum is simply dummy text of the printing and typesetting industry. &nbsp;Simply dummy.</p>
  <small>DANA MERCER, OWNER</small>
</section>
<div class="abs avatar" role="img" aria-label="Portrait photo of the owner"></div>

<footer class="abs footer">
  <h4 style="left:86px">CONTACT INFORMATION</h4>
  <h4 style="left:425px">RECENT BLOG POSTS</h4>
  <h4 style="left:738px">QUICK LINKS</h4>
  <h4 style="left:928px">NEWSLETTER</h4>
</footer>

<div class="contact-row" style="top:2582px;color:#fff"><span class="ic"><svg width="12" height="14" viewBox="0 0 12 14"><path d="M6 0a5 5 0 0 1 5 5c0 4-5 9-5 9S1 9 1 5a5 5 0 0 1 5-5z" fill="#fff"/><circle cx="6" cy="5" r="2" fill="#141414"/></svg></span><span>K &amp; T FIRE SAFETY EQUIPMENT INC<br>1200 N CEDAR ST, KISSIMMEE,<br>United States</span></div>
<div class="contact-row" style="top:2654px;color:#fff;font-size:14px"><span class="ic"><svg width="14" height="14" viewBox="0 0 14 14"><path d="M3 1l3 3-2 2a8 8 0 0 0 4 4l2-2 3 3-2 2C6 13 1 8 1 3z" fill="#fff"/></svg></span><span style="line-height:30px">1-407-555-0142</span></div>
<div class="contact-row" style="top:2702px;color:#fff"><span class="ic"><svg width="14" height="10" viewBox="0 0 14 10"><rect x="0" y="0" width="14" height="10" fill="#fff"/><path d="M0 0l7 6 7-6" fill="none" stroke="#141414"/></svg></span><span style="line-height:30px">info@kandtfiresafety.example</span></div>

<div class="abs vdiv" style="left:372px"></div>
<div class="post" style="top:2580px;color:#fff"><div class="date">November 19, 2016</div>The sight of the tumblers restored Bob Sawyer ...</div>
<div class="abs" style="left:425px;top:2658px;width:250px;height:1px;background:#2c2c2c"></div>
<div class="post" style="top:2675px;color:#fff"><div class="date">November 19, 2016</div>The sight of the tumblers restored Bob Sawyer to ...</div>
<div class="abs vdiv" style="left:681px"></div>
<ul class="abs links"><li>Home</li><li>Services</li><li>Testimonials</li><li>Jobs</li><li>Contact Us</li></ul>
<div class="abs vdiv" style="left:884px"></div>
<div class="abs news-input">Your Email Id...</div>
<div class="abs btn news-go">GO</div>
<div class="abs soc" style="left:936px"></div>
<div class="abs soc" style="left:969px"></div>
<div class="abs soc" style="left:1002px"></div>
<div class="abs soc" style="left:1035px"></div>

<div class="abs copy">© 2018. My company. All Rights Reserved.</div>

</body>
</html>
```